Business cards for start-up accounting firm

I'm looking for a double sided business card ready for upload into Lumo print or similar print providers with no modification required by me.
I'm looking for something simple as i think cards that are too 'busy' actually detract from the message. I have some thoughts but more than happy to see what comes up. The logo i have came out of left field and i love it the moment i saw it!

My thoughts:

Side 1: Just the logo, perhaps on a dark grey or charcoal background to make the logo colours stand out?

Side 2: The call to action from me website 'Looking for a more relaxed, friendly and interactive relationship with your accountant?' with my contact information
Name: Gus Tarrow
Email: gus@ledgerowl.com.au
Website: www.ledgerowl.com.au
Phone: 1300 762 349

The call to action needs to be the first thing they see when they look at side 2. If it helps to know what we do and how we do it there is a draft website at www.ledgerowl.com.au

Like i said, happy to consider anything that comes up :)

Target Market(s)

i'm targeting small business owners who experience a lot of stress around finacial reporting and have had bad experiences with accountants in the past.

Industry/Entity Type

Accounting

Contact Information for Business Card

Contained in the Description

Font styles to use
Serif
Sans Serif
Other font styles liked:
• See logo files attached

Colors
474747

Requirements
Must have
• My logo, slogan and contact information

```html
<!DOCTYPE html>
<html lang="en">
<head>
<meta charset="utf-8">
<title>Ledger Owl — Business Card</title>
<link rel="stylesheet" href="https://fonts.googleapis.com/css2?family=Crimson+Text:wght@400;600;700&family=Ubuntu:wght@400;500&display=swap">
<style>
  :root {
    --backdrop: #3a3a3a;
    --card: #070707;
    --yellow: #ffd60a;
    --purple: #8a3a7e;
    --white: #ffffff;
    --divider: #8a8a8a;
  }
  * { margin: 0; padding: 0; box-sizing: border-box; }
  html, body { width: 1200px; height: 1200px; overflow: hidden; }
  body { background: var(--backdrop); position: relative; font-family: "Crimson Text", Georgia, serif; }

  .card { position: absolute; left: 119px; width: 962px; background: var(--card); }
  .card--contact { top: 30px; height: 549px; }
  .card--brand { top: 620px; height: 549px; }

  .cta-banner {
    position: absolute; left: 0; top: 10px; width: 926px; height: 90px;
    background: var(--yellow); border-radius: 0 45px 45px 0;
    padding: 8px 20px 0 30px;
    color: var(--white); font-size: 27px; font-weight: 600; line-height: 37px; letter-spacing: 0.4px;
  }

  .holder-name {
    position: absolute; left: 89px; top: 290px;
    color: var(--purple); font-size: 46px; font-weight: 600; letter-spacing: 0.3px;
  }

  .mini-brand { position: absolute; left: 32px; top: 476px; }
  .mini-brand__name { color: var(--yellow); font-size: 19px; font-weight: 700; line-height: 1; letter-spacing: 0.5px; }
  .mini-brand__tag { color: var(--purple); font-family: "Ubuntu", Arial, sans-serif; font-size: 6px; letter-spacing: 0.8px; margin-top: 4px; }

  .divider { position: absolute; left: 479px; top: 175px; width: 2px; height: 300px; background: var(--divider); }

  .contact-list { position: absolute; left: 492px; top: 185px; list-style: none; }
  .contact-item { position: absolute; left: 0; display: flex; align-items: center; white-space: nowrap; }
  .contact-item svg { width: 42px; height: 42px; flex: none; }
  .contact-item span { margin-left: 27px; color: var(--white); }
  .contact-item--phone { top: 0; }
  .contact-item--phone span { font-size: 27px; font-weight: 600; }
  .contact-item--email { top: 110px; }
  .contact-item--email span { font-family: Arial, Helvetica, sans-serif; font-size: 26px; margin-left: 25px; }
  .contact-item--web { top: 232px; }
  .contact-item--web span { font-size: 27px; font-weight: 600; }

  .brand-lockup { position: absolute; left: 0; right: 0; top: 190px; text-align: center; }
  .brand-lockup__name { color: var(--yellow); font-size: 100px; font-weight: 700; line-height: 1; letter-spacing: 2px; }
  .brand-lockup__slogan {
    display: flex; align-items: center; justify-content: center; gap: 18px; margin-top: 72px;
    color: var(--purple); font-family: "Ubuntu", Arial, sans-serif; font-size: 25px; letter-spacing: 3.5px;
  }
  .brand-lockup__slogan::before, .brand-lockup__slogan::after {
    content: ""; width: 66px; height: 2px; background: var(--purple);
  }
</style>
</head>
<body>
  <section class="card card--contact">
    <p class="cta-banner">Looking for a more relaxed, friendly and interactive relationship with your accountant?</p>
    <h1 class="holder-name">Gus Tarrow</h1>
    <div class="mini-brand">
      <div class="mini-brand__name">LEDGER OWL</div>
      <div class="mini-brand__tag">CALM BOOKS, CLEAR GROWTH</div>
    </div>
    <div class="divider"></div>
    <ul class="contact-list">
      <li class="contact-item contact-item--phone">
        <svg viewBox="0 0 24 24" aria-hidden="true"><path fill="#ffd60a" d="M6.6 2.5c.6-.3 1.3 0 1.6.5l1.9 3.4c.3.6.2 1.3-.3 1.7L8.3 9.3c.9 2.3 3.1 4.6 5.6 5.7l1.3-1.5c.4-.5 1.1-.6 1.7-.3l3.4 1.8c.6.3.8 1 .6 1.6l-.7 2.2c-.3.9-1.2 1.5-2.1 1.4C9.8 19.6 3.9 13.6 3.3 5.3c-.1-.9.5-1.8 1.3-2.1z"/></svg>
        <span>1300 762 349</span>
      </li>
      <li class="contact-item contact-item--email">
        <svg viewBox="0 0 24 24" aria-hidden="true"><g fill="none" stroke="#ffd60a" stroke-width="1.8" stroke-linejoin="round"><path d="M3 10 12 4l9 6v10H3z"/><path d="M3 10l9 6 9-6M3 20l7-5M21 20l-7-5"/></g></svg>
        <span>gus@ledgerowl.com.au</span>
      </li>
      <li class="contact-item contact-item--web">
        <svg viewBox="0 0 24 24" aria-hidden="true"><g fill="none" stroke="#ffd60a" stroke-width="1.4"><circle cx="12" cy="12" r="9"/><ellipse cx="12" cy="12" rx="4" ry="9"/><path d="M3 12h18M4.5 7.5h15M4.5 16.5h15M12 3v18"/></g></svg>
        <span>www.ledgerowl.com.au</span>
      </li>
    </ul>
  </section>

  <section class="card card--brand">
    <div class="brand-lockup">
      <div class="brand-lockup__name">LEDGER OWL</div>
      <div class="brand-lockup__slogan">CALM BOOKS, CLEAR GROWTH</div>
    </div>
  </section>
</body>
</html>
```